I am a new company with the latest technology in the concrete polishing business

We need a logo design for a new company out of Toronto, Canada. We polish residential, commercial and industrial concrete as well as different epoxy toppings.

Target Market(s)

How Owners with expendable incomes

Industry/Entity Type

Construction

Contact Information for Business Card

be able to see content rather easily

Colors
0355a3
fbed22
1b1b1b

Requirements
Must have
• simple and elegant

```html
<!DOCTYPE html>
<html lang="en">
<head>
<meta charset="utf-8">
<title>Slabline Coatings – Business Card</title>
<link rel="stylesheet" href="https://fonts.googleapis.com/css2?family=Lato:wght@400;700&display=swap">
<style>
  :root {
    --brand-blue: #0355a3;
    --card-blue: #0b57a4;
    --ink: #1b1b1b;
    --paper: #ffffff;
    --stage: #2a2a2a;
    --muted: #3a3a3a;
  }
  * { box-sizing: border-box; margin: 0; padding: 0; }
  html, body { width: 1200px; height: 880px; overflow: hidden; }
  body {
    background: var(--stage);
    font-family: "Lato", Arial, sans-serif;
    display: flex;
    flex-direction: column;
    align-items: center;
    justify-content: center;
    gap: 40px;
  }
  .card {
    width: 640px;
    height: 366px;
    border-radius: 26px;
    position: relative;
    overflow: hidden;
  }
  .card--front {
    background: var(--card-blue);
    color: var(--paper);
    display: flex;
    flex-direction: column;
    align-items: center;
    justify-content: center;
    gap: 22px;
  }
  .brand-square {
    width: 92px;
    height: 92px;
    border: 5px solid currentColor;
    border-radius: 14px;
  }
  .brand-name {
    font-size: 30px;
    font-weight: 400;
    letter-spacing: 1px;
  }
  .card--back {
    background: var(--paper);
    display: grid;
    grid-template-columns: 1fr 1px 1fr;
    align-items: center;
  }
  .back-brand {
    display: flex;
    flex-direction: column;
    align-items: center;
    gap: 18px;
    color: var(--brand-blue);
    padding-top: 70px;
  }
  .back-brand .brand-square { width: 78px; height: 78px; border-width: 4px; }
  .back-brand .brand-name { font-size: 26px; }
  .divider {
    width: 1px;
    height: 150px;
    background: var(--brand-blue);
    align-self: center;
    margin-top: 30px;
  }
  .contact { padding-left: 34px; color: var(--ink); }
  .person-name { font-size: 22px; font-weight: 700; line-height: 1.1; }
  .person-name .surname { color: var(--brand-blue); font-weight: 400; }
  .person-title { font-size: 14px; margin-bottom: 14px; color: var(--muted); }
  .contact-list { list-style: none; display: flex; flex-direction: column; gap: 6px; }
  .contact-item { display: flex; align-items: center; gap: 8px; font-size: 14px; }
  .contact-icon { width: 18px; height: 18px; flex: none; }
</style>
</head>
<body>
  <section class="card card--front" aria-label="Card front">
    <div class="brand-square"></div>
    <p class="brand-name">Slabline Coatings</p>
  </section>

  <section class="card card--back" aria-label="Card back">
    <div class="back-brand">
      <div class="brand-square"></div>
      <p class="brand-name">Slabline Coatings</p>
    </div>
    <div class="divider"></div>
    <div class="contact">
      <p class="person-name">Marek <span class="surname">Dalton</span></p>
      <p class="person-title">President</p>
      <ul class="contact-list">
        <li class="contact-item">
          <svg class="contact-icon" viewBox="0 0 18 18"><circle cx="9" cy="9" r="8" fill="none" stroke="#0355a3" stroke-width="1.3"/><rect x="6.3" y="4.3" width="5.4" height="9.4" rx="1" fill="none" stroke="#0355a3" stroke-width="1.2"/></svg>
          (416) 555 0142
        </li>
        <li class="contact-item">
          <svg class="contact-icon" viewBox="0 0 18 18"><circle cx="9" cy="9" r="8" fill="none" stroke="#0355a3" stroke-width="1.3"/><rect x="4.5" y="6" width="9" height="6" fill="none" stroke="#0355a3" stroke-width="1.2"/><path d="M4.5 6 9 9.5 13.5 6" fill="none" stroke="#0355a3" stroke-width="1.2"/></svg>
          info@slablinemail.com
        </li>
        <li class="contact-item">
          <svg class="contact-icon" viewBox="0 0 18 18"><circle cx="9" cy="9" r="8" fill="none" stroke="#0355a3" stroke-width="1.3"/><circle cx="9" cy="9" r="4.5" fill="none" stroke="#0355a3" stroke-width="1.1"/><path d="M4.5 9h9M9 4.5c-2 2.5-2 6.5 0 9M9 4.5c2 2.5 2 6.5 0 9" fill="none" stroke="#0355a3" stroke-width="1"/></svg>
          www.slablineweb.com
        </li>
      </ul>
    </div>
  </section>
</body>
</html>
```